The dental corner of brindlewood web page

website for dental office
Already have domain, mostly information only with address, telephone and google map and hours of operation on top. mobile friendly. SEO a most.

Target Market(s)

Local families

Industry/Entity Type

Dental Clinic

Number of Pages Required

1 page

Font styles to use
Serif

Colors

Designer to choose colors to be used in the design.

Requirements
Must have
• SEO
• Information to find the location
• mobile friendly
• dr's. biography
• services offered
• contect to social media (google, facebook, and instagram)
• Se habla espaƱol
• All insurance accepted
• request an appointment form to notify us

```html
<!DOCTYPE html>
<html lang="en">
<head>
<meta charset="utf-8">
<title>The Dental Corner of Brindlewood</title>
<link href="https://fonts.googleapis.com/css2?family=Cinzel:wght@400;700&family=Open+Sans:wght@400;600;700&display=swap" rel="stylesheet">
<style>
:root{
  --blue:#0b4fae;
  --blue-dark:#083c86;
  --green:#8cc63f;
  --green-dark:#6fa82a;
  --ink:#333;
  --muted:#777;
  --light:#f4f6f9;
  --footer:#1d2126;
  --white:#fff;
}
*{box-sizing:border-box;margin:0;padding:0}
html,body{width:1200px;height:3805px;overflow:hidden}
body{font-family:"Open Sans",Arial,sans-serif;color:var(--ink);background:var(--white);position:relative}
.serif{font-family:"Cinzel",Georgia,serif}
.wrap{width:820px;margin:0 auto;position:relative}
section,header,footer{position:absolute;left:0;width:1200px}
.title{font-family:"Cinzel",Georgia,serif;font-size:30px;text-align:center;letter-spacing:1px}
.title .g{color:var(--green)}
.divider{display:flex;align-items:center;justify-content:center;gap:8px;margin:6px auto 0}
.divider i{display:block;width:70px;height:2px;background:currentColor;opacity:.6}
.divider b{display:block;width:14px;height:14px;border:2px solid currentColor;border-radius:50%}
.btn{display:inline-block;background:var(--blue);color:#fff;font-size:11px;font-weight:700;letter-spacing:1px;padding:9px 22px;border-radius:20px;text-transform:uppercase}
.ph{display:block}

/* header */
.site-header{top:0;height:100px;background:#fff;box-shadow:0 2px 6px rgba(0,0,0,.08);z-index:5}
.logo{position:absolute;left:130px;top:18px;display:flex;align-items:center;gap:8px}
.logo .dot{width:40px;height:40px;border-radius:50%;background:var(--blue)}
.logo span{font-family:"Cinzel",Georgia,serif;font-size:13px;color:var(--blue);font-weight:700;width:130px;line-height:1.2}
.topbar{position:absolute;right:0;top:0;width:800px;height:30px;background:var(--green);border-bottom-left-radius:30px;display:flex;align-items:center;gap:30px;padding-left:50px;color:#fff;font-size:11px}
.topbar .item{display:flex;align-items:center;gap:6px}
.topbar .lang{margin-left:auto;margin-right:28px;display:flex;align-items:center;gap:4px}
.topbar .lang b{width:18px;height:18px;border-radius:50%;background:#e8b21c;display:block}
.nav{position:absolute;right:130px;top:56px;display:flex;gap:52px;font-size:12px;color:var(--blue);text-transform:uppercase;letter-spacing:.5px}
.nav a.on{border-bottom:2px solid var(--blue);padding-bottom:6px;font-weight:700}

/* hero */
.hero{top:100px;height:560px;background:linear-gradient(100deg,#eef3f8 0%,#dde7f0 45%,#c9d7e6 100%)}
.hero .photo{position:absolute;inset:0}
.hero-copy{position:absolute;left:210px;top:200px;text-align:center;width:320px}
.hero-copy h1{font-family:"Cinzel",Georgia,serif;font-size:36px;color:var(--blue);font-weight:400;letter-spacing:1px}
.hero-copy h2{font-family:"Cinzel",Georgia,serif;font-size:22px;color:var(--green);font-weight:400;border-top:1px solid var(--green);border-bottom:1px solid var(--green);display:inline-block;padding:0 10px;margin:4px 0 14px}
.hero-wave{position:absolute;left:0;bottom:0}

/* welcome */
.welcome{top:660px;height:320px;text-align:center;padding-top:40px}
.welcome .title{color:var(--blue)}
.welcome .sub{font-family:"Cinzel",Georgia,serif;font-size:12px;color:var(--green);margin:-4px 0 0 340px}
.welcome .lead{font-family:"Cinzel",Georgia,serif;font-weight:700;font-size:14px;margin:22px 0 10px}
.welcome p{font-size:11px;color:var(--muted);line-height:1.8;width:800px;margin:0 auto 18px}

/* services */
.services{top:982px;height:390px;background:linear-gradient(120deg,var(--blue) 0%,#1462c4 50%,var(--blue-dark) 100%);color:#fff;text-align:center;padding-top:45px}
.services .divider{color:#fff}
.svc-row{display:flex;justify-content:center;gap:30px;margin-top:40px}
.svc{width:165px}
.svc .icon{width:86px;height:86px;border-radius:50%;background:#fff;margin:0 auto 16px;border:6px solid rgba(255,255,255,.35);background-clip:padding-box}
.svc h3{font-size:13px;letter-spacing:.5px;font-weight:700}
.svc p{font-size:10px;opacity:.85;line-height:1.5;margin:6px 0 12px}
.svc .line{display:flex;align-items:center;gap:6px;justify-content:center}
.svc .line i{width:50px;height:1px;background:rgba(255,255,255,.6)}
.svc .line b{width:16px;height:16px;border-radius:50%;background:#fff}
.arrow{position:absolute;top:50%;width:20px;height:30px}

/* bio */
.bio{top:1372px;height:520px;background:#fff;padding-top:45px}
.bio .title{color:var(--blue)}
.bio .divider{color:var(--green)}
.bio-body{display:flex;gap:60px;width:820px;margin:40px auto 0}
.bio-photo{position:relative;width:280px;height:280px;flex:none}
.bio-photo .ring{position:absolute;inset:0;border-radius:50%;border:8px solid var(--blue)}
.bio-photo .img{position:absolute;inset:14px;border-radius:50%;background:linear-gradient(160deg,#e7edf2,#c7d3de)}
.social{position:absolute;right:-10px;display:flex;flex-direction:column;gap:8px;top:140px}
.social b{display:block;width:30px;height:30px;border-radius:50%}
.bio-text h4{font-size:13px;font-weight:600;letter-spacing:.5px;margin:10px 0 14px}
.bio-text p{font-size:11px;color:var(--muted);line-height:1.9;margin-bottom:20px}

/* reviews */
.reviews{top:1892px;height:305px;background:linear-gradient(90deg,var(--green-dark),var(--green) 50%,#a3d35c);color:#fff;text-align:center;padding-top:40px}
.reviews .divider{color:#fff}
.review-row{display:flex;justify-content:center;gap:40px;margin-top:35px}
.review{display:flex;gap:18px;align-items:center;width:400px;text-align:left}
.review .avatar{width:100px;height:100px;border-radius:50%;background:#e7eef4;border:4px solid #fff;flex:none}
.review p{font-size:10px;line-height:1.6}
.review .name{font-family:"Cinzel",Georgia,serif;font-size:11px;margin-top:8px}
.review .stars{color:#1b3f8a;letter-spacing:1px;margin-left:6px}

/* blog */
.blog{top:2197px;height:500px;background:#fff;padding-top:45px}
.blog .title{color:var(--blue)}
.blog .divider{color:var(--green)}
.posts{display:flex;gap:20px;justify-content:center;margin-top:30px}
.post{width:235px;background:#fff;box-shadow:0 4px 14px rgba(0,0,0,.12)}
.post .img{height:160px;position:relative}
.post .date{position:absolute;left:10px;top:0;width:40px;background:var(--blue);color:#fff;text-align:center;font-weight:700;font-size:16px;padding:4px 0}
.post .date small{display:block;font-size:8px;background:var(--green)}
.post h3{font-family:"Cinzel",Georgia,serif;font-size:12px;color:var(--blue);text-align:center;padding:12px 14px 6px;line-height:1.3}
.post p{font-size:10px;color:var(--muted);text-align:center;padding:0 16px 16px;line-height:1.6}

/* insurance */
.insurance{top:2697px;height:80px;background:var(--blue);display:flex;align-items:center}
.insurance h2{font-family:"Cinzel",Georgia,serif;font-size:28px;color:#fff;font-weight:400;margin-left:215px}
.insurance .cta{margin-left:150px;background:var(--green);color:#fff;font-size:11px;font-weight:700;padding:10px 26px;border-radius:20px;letter-spacing:.5px}

/* form */
.appointment{top:2777px;height:415px;background:#f2f4f7;padding-top:40px}
.appointment .title{color:var(--blue)}
.appointment .divider{color:var(--green)}
.form{width:785px;margin:40px auto 0}
.row{display:flex;gap:12px;margin-bottom:12px}
.field{flex:1;height:34px;background:#fff;border:1px solid #dde2e8;font-size:10px;color:#999;padding:10px 10px;display:flex;justify-content:space-between}
.field.msg{height:80px}
.submit{display:block;width:150px;margin:20px auto 0;text-align:center}

/* map */
.map{top:3192px;height:263px;background:linear-gradient(180deg,#eef0ea,#e3e6df)}

/* footer */
.site-footer{top:3455px;height:322px;background:linear-gradient(180deg,#23282e,var(--footer));color:#ddd}
.cols{display:flex;width:820px;margin:0 auto;padding-top:38px;gap:28px}
.col h4{font-family:"Cinzel",Georgia,serif;color:#fff;font-size:15px;font-weight:400;letter-spacing:1px;padding-bottom:8px;border-bottom:2px solid var(--green);display:inline-block;margin-bottom:16px}
.col ul{list-style:none;font-size:10px;line-height:2.4}
.col ul li:before{content:"› ";color:var(--green)}
.contact div{display:flex;gap:10px;margin-bottom:14px;font-size:10px;line-height:1.5}
.contact strong{display:block;color:#fff;font-size:12px}
.hours{font-size:10px;line-height:2.2}
.hours span{display:inline-block;width:70px;color:#fff;font-weight:700}
.cards{display:flex;gap:6px;margin-top:6px}
.cards b{width:32px;height:20px;background:#f3f3f3;border-radius:2px;display:block}
.follow{text-align:center}
.follow .logo-f{display:flex;flex-direction:column;align-items:center;gap:8px;margin:10px 0 14px}
.follow .logo-f i{width:42px;height:42px;border-radius:50%;border:2px solid #fff;display:block}
.follow .logo-f span{font-family:"Cinzel",Georgia,serif;font-size:12px;color:#fff;width:140px}
.follow .icons{display:flex;gap:8px;justify-content:center}
.follow .icons b{width:26px;height:26px;border:1px solid #fff;border-radius:50%;display:block}
.copyright{top:3777px;height:28px;background:var(--blue);color:#fff;font-size:9px;display:flex;align-items:center;padding:0 210px;justify-content:space-between}
</style>
</head>
<body>

<header class="site-header">
  <div class="logo"><i class="dot"></i><span>The Dental Corner of Brindlewood</span></div>
  <div class="topbar">
    <div class="item">
      <svg width="12" height="12" viewBox="0 0 24 24" fill="#fff"><path d="M6.6 10.8a15 15 0 0 0 6.6 6.6l2.2-2.2c.3-.3.7-.4 1-.2 1.1.4 2.3.6 3.6.6.6 0 1 .4 1 1V20c0 .6-.4 1-1 1A17 17 0 0 1 3 4c0-.6.4-1 1-1h3.5c.6 0 1 .4 1 1 0 1.3.2 2.5.6 3.6.1.3 0 .7-.2 1z"/></svg>
      (555) 014-2290</div>
    <div class="item">
      <svg width="12" height="12" viewBox="0 0 24 24" fill="none" stroke="#fff" stroke-width="2"><circle cx="12" cy="12" r="9"/><path d="M12 7v5l3 2"/></svg>
      MON-SAT 8:00AM TO 6:00PM</div>
    <div class="item">
      <svg width="12" height="12" viewBox="0 0 24 24" fill="#fff"><path d="M12 2a7 7 0 0 0-7 7c0 5 7 13 7 13s7-8 7-13a7 7 0 0 0-7-7zm0 9.5A2.5 2.5 0 1 1 12 6.5a2.5 2.5 0 0 1 0 5z"/></svg>
      4180 Linden Grove Rd, Suite 115, Brindlewood, FL 30000</div>
    <div class="lang"><b></b> ES ▾</div>
  </div>
  <nav class="nav">
    <a class="on">Home</a><a>About Us</a><a>Services</a><a>Dr's Biography</a><a>Blog</a><a>Contact Us</a>
  </nav>
</header>

<section class="hero">
  <div class="photo" role="img" aria-label="Photo of a smiling patient in a dental chair with a dentist in the background"></div>
  <div class="hero-copy">
    <h1>A Beautiful Smile</h1>
    <h2>Can Be Yours</h2><br>
    <span class="btn">Make an Appointment</span>
  </div>
  <svg class="hero-wave" width="1200" height="90" viewBox="0 0 1200 90" preserveAspectRatio="none">
    <path d="M0 20 Q600 120 1200 0 L1200 90 L0 90Z" fill="#fff"/>
    <path d="M0 20 Q600 120 1200 0" fill="none" stroke="#0b4fae" stroke-width="4"/>
    <path d="M0 30 Q600 130 1200 10" fill="none" stroke="#8cc63f" stroke-width="2"/>
  </svg>
</section>

<section class="welcome">
  <h2 class="title"><span class="g">Welcome</span> <span style="color:var(--blue)">to the Dental Corner</span></h2>
  <div class="sub">of Brindlewood</div>
  <div class="lead">Gentle care for every smile in the family, close to home and easy to reach.</div>
  <p>We welcome children, parents and grandparents with calm, modern dentistry. Our team offers checkups, cleanings, fillings and more in a friendly office. We accept all insurance plans and se habla español. Book a visit online or call us and we will find a time that fits your week.</p>
  <span class="btn">Read More</span>
</section>

<section class="services">
  <h2 class="title">Services We Offer</h2>
  <div class="divider"><i></i><b></b><i></i></div>
  <svg class="arrow" style="left:140px" viewBox="0 0 20 30"><path d="M15 3 L4 15 L15 27" stroke="#fff" stroke-width="2" fill="none"/></svg>
  <svg class="arrow" style="right:140px" viewBox="0 0 20 30"><path d="M5 3 L16 15 L5 27" stroke="#fff" stroke-width="2" fill="none"/></svg>
  <div class="svc-row">
    <div class="svc"><div class="icon"></div><h3>DIAGNOSTICS</h3><p>Exams and digital x-rays that find small issues early.</p><div class="line"><i></i><b></b><i></i></div></div>
    <div class="svc"><div class="icon"></div><h3>ORAL SURGERY</h3><p>Safe extractions and minor procedures done with care.</p><div class="line"><i></i><b></b><i></i></div></div>
    <div class="svc"><div class="icon"></div><h3>RESTORATIONS</h3><p>Fillings and crowns that bring back strength and shape.</p><div class="line"><i></i><b></b><i></i></div></div>
    <div class="svc"><div class="icon"></div><h3>ENDODONTICS</h3><p>Root canal care that relieves pain and saves teeth.</p><div class="line"><i></i><b></b><i></i></div></div>
  </div>
</section>

<section class="bio">
  <h2 class="title">Dr's Biography</h2>
  <div class="divider"><i></i><b></b><i></i></div>
  <div class="bio-body">
    <div class="bio-photo">
      <div class="ring"></div>
      <div class="img" role="img" aria-label="Portrait of the dentist in a white coat"></div>
      <div class="social" aria-label="Social media links">
        <b style="background:#e04a3a"></b><b style="background:#2c4f9a"></b><b style="background:#6a8fc8"></b>
      </div>
    </div>
    <div class="bio-text">
      <h4>DR. MAREN ELISE HOLLOWAY , DDS</h4>
      <p>Dr. Holloway has cared for local families for over fifteen years. She earned her dental degree with honors and completed advanced training in restorative and family dentistry. She believes every visit should feel calm and clear, so she takes time to explain each step and answer every question. Outside the office she volunteers at school health fairs, teaching children how to brush and floss. She speaks English and Spanish and loves helping nervous patients feel at ease. Her goal is simple: healthy, confident smiles for every member of the family, from a first tooth to a lifetime of care.</p>
      <span class="btn">Read More</span>
    </div>
  </div>
</section>

<section class="reviews">
  <h2 class="title">Patient's Reviews</h2>
  <div class="divider"><i></i><b></b><i></i></div>
  <svg class="arrow" style="left:140px;top:145px" viewBox="0 0 20 30"><path d="M15 3 L4 15 L15 27" stroke="#fff" stroke-width="2" fill="none"/></svg>
  <svg class="arrow" style="right:140px;top:145px" viewBox="0 0 20 30"><path d="M5 3 L16 15 L5 27" stroke="#fff" stroke-width="2" fill="none"/></svg>
  <div class="review-row">
    <div class="review"><div class="avatar" role="img" aria-label="Patient portrait"></div><div><p>"The whole team was kind and patient. My kids now look forward to their checkups...[+]"</p><div class="name">Nora Whitfield <span class="stars">★★★★★</span></div></div></div>
    <div class="review"><div class="avatar" role="img" aria-label="Patient portrait"></div><div><p>"Easy booking, friendly staff and a gentle doctor. I finally feel calm at the dentist...[+]"</p><div class="name">Celia Marsh <span class="stars">★★★★★</span></div></div></div>
  </div>
</section>

<section class="blog">
  <h2 class="title"><span class="g">Our</span> Blog</h2>
  <div class="divider"><i></i><b></b><i></i></div>
  <svg class="arrow" style="left:140px;top:230px" viewBox="0 0 20 30"><path d="M15 3 L4 15 L15 27" stroke="#555" stroke-width="2" fill="none"/></svg>
  <svg class="arrow" style="right:140px;top:230px" viewBox="0 0 20 30"><path d="M5 3 L16 15 L5 27" stroke="#555" stroke-width="2" fill="none"/></svg>
  <div class="posts">
    <div class="post"><div class="img" role="img" aria-label="Photo of a parent and child brushing teeth" style="background:linear-gradient(135deg,#dfe8f1,#b9cde0)"><div class="date">14<small>SEP</small></div></div><h3>Brushing Habits for Little Smiles</h3><p>Simple tips that help children build a healthy routine at home and enjoy it...[+]</p></div>
    <div class="post"><div class="img" role="img" aria-label="Photo of a dental treatment room" style="background:linear-gradient(135deg,#e4ecef,#bcd3dc)"><div class="date">15<small>SEP</small></div></div><h3>What to Expect at a Checkup</h3><p>A short guide to each step of a routine visit so first-timers feel at ease...[+]</p></div>
    <div class="post"><div class="img" role="img" aria-label="Photo of a dentist showing x-rays to a patient" style="background:linear-gradient(135deg,#e8e4ea,#c6c1d2)"><div class="date">13<small>SEP</small></div></div><h3>Why Digital X-Rays Matter</h3><p>Learn how modern imaging finds problems early with lower exposure for all...[+]</p></div>
  </div>
</section>

<section class="insurance">
  <h2>We Accept All Insurance</h2>
  <span class="cta">▣ SCHEDULE AN APPOINTMENT</span>
</section>

<section class="appointment">
  <h2 class="title"><span class="g">Appointment</span> Form</h2>
  <div class="divider"><i></i><b></b><i></i></div>
  <div class="form">
    <div class="row"><div class="field">Name</div><div class="field">Email</div><div class="field">Phone</div></div>
    <div class="row"><div class="field">Select Date <span>▦</span></div><div class="field">Time <span>◷</span></div><div class="field">Select Services <span>▾</span></div></div>
    <div class="row"><div class="field msg">Message</div></div>
    <span class="btn submit">Submit Now</span>
  </div>
</section>

<section class="map" role="img" aria-label="Street map showing the office location"></section>

<footer class="site-footer">
  <div class="cols">
    <div class="col" style="width:150px"><h4>Quick Links</h4>
      <ul><li>HOME</li><li>ABOUT US</li><li>SERVICES</li><li>DR'S BIOGRAPHY</li><li>BLOG</li><li>CONTACT US</li></ul></div>
    <div class="col contact" style="width:210px"><h4>Contact Detail</h4>
      <div><span style="color:var(--green)">●</span><p><strong>ADDRESS</strong>4180 Linden Grove Rd, Suite 115, Brindlewood, FL 30000</p></div>
      <div><span style="color:var(--green)">●</span><p><strong>PHONE</strong>(555) 014-2290</p></div>
      <div><span style="color:var(--green)">●</span><p><strong>EMAIL</strong>info@dentalcornerbrindlewood.com</p></div></div>
    <div class="col" style="width:210px"><h4>Office Hours</h4>
      <div class="hours"><div><span>MONDAY</span>9:00 AM - 5:00 PM</div><div><span>TUESDAY</span>9:00 AM - 5:00 PM</div><div><span>WEDNESDAY</span>9:00 AM - 5:00 PM</div><div><span>THURSDAY</span>9:00 AM - 5:00 PM</div></div>
      <h4 style="margin-top:14px;border:none;margin-bottom:4px">We Accept</h4>
      <div class="cards" aria-label="Accepted payment cards"><b></b><b></b><b></b><b></b></div></div>
    <div class="col follow" style="width:170px"><h4>Follow Us On</h4>
      <div class="logo-f"><i></i><span>The Dental Corner of Brindlewood</span></div>
      <div class="icons" aria-label="Social media links"><b></b><b></b><b></b></div></div>
  </div>
</footer>

<section class="copyright"><span>COPYRIGHT © 2018 THE DENTAL CORNER OF BRINDLEWOOD. ALL RIGHT RESERVED</span><span>PRIVACY &nbsp;&nbsp; TERMS OF USE</span></section>

</body>
</html>
```